Business Card Design Project

We need a Business Card for an Mechanical Engineering firm in Singapore. The design should be Modern & Technical looking, yet eye catching.

Our company deals in Cutting Tools & Machine Accessories for the Manufacturing Industries such as Oil & Gas, Aero Space, etc... For more information on our Company, you can either email me or view our website www.valtrion.com.sg.

We are trying to revamp our image to give our consumers a fresh new perspective to our company, so we welcome all ideas.

Industry/Entity Type

Business

Requirements
Must have
• Must incorporate New Company Logo into the card as shown in Uploaded file.

```html
<!DOCTYPE html>
<html lang="en">
<head>
<meta charset="utf-8">
<title>Valtrion Tools – Business Card Set</title>
<link rel="stylesheet" href="https://fonts.googleapis.com/css2?family=Saira+Extra+Condensed:wght@300;400&display=swap">
<style>
  :root {
    --page-bg: #ffffff;
    --card-white: #ffffff;
    --card-red: #951a2f;
    --card-black: #231f20;
    --ink-dark: #231f20;
    --ink-red: #951a2f;
    --ink-light: #ffffff;
    --card-shadow: 0 10px 14px rgba(0,0,0,0.35);
    --type-face: "Saira Extra Condensed", "Liberation Sans Narrow", "Arial Narrow", "Roboto Condensed", sans-serif;
  }
  * { margin: 0; padding: 0; box-sizing: border-box; }
  html, body {
    width: 1200px; height: 841px; overflow: hidden;
    background: var(--page-bg);
  }
  .canvas { position: relative; width: 1200px; height: 841px; }

  .card {
    position: absolute;
    width: 438px; height: 283px;
    overflow: hidden;
    box-shadow: var(--card-shadow);
    font-family: var(--type-face);
    font-weight: 300;
  }
  .card--front-white { left: 87px;  top: 84px;  background: var(--card-white); }
  .card--front-red   { left: 667px; top: 84px;  background: var(--card-red); }
  .card--back        { left: 383px; top: 459px; width: 436px; height: 284px; background: var(--card-black); }

  .gear-artwork { position: absolute; inset: 0; width: 100%; height: 100%; }

  .contact {
    position: absolute; left: 258px; top: 0; width: 175px; height: 100%;
  }
  .contact p {
    position: absolute; left: 0;
    white-space: nowrap; line-height: 1;
  }
  .contact__name    { top: 150px; font-size: 21px; }
  .contact__phone   { top: 185px; font-size: 21px; letter-spacing: 0.3px; }
  .contact__address { top: 211px; font-size: 15px; }
  .contact__web     { top: 233px; font-size: 15px; }
  .contact__email   { top: 255px; font-size: 15px; }

  .card--front-white .contact__name { color: var(--ink-dark); }
  .card--front-white .contact__phone,
  .card--front-white .contact__address,
  .card--front-white .contact__web,
  .card--front-white .contact__email { color: var(--ink-red); }

  .card--front-red .contact__name { color: var(--ink-light); }
  .card--front-red .contact__phone,
  .card--front-red .contact__address,
  .card--front-red .contact__web,
  .card--front-red .contact__email { color: var(--ink-dark); }

  .brand {
    position: absolute; left: 0; right: 0; top: 152px;
    display: flex; align-items: center; justify-content: center; gap: 10px;
  }
  .brand__mark {
    width: 28px; height: 28px; border-radius: 50%;
    background: var(--ink-red);
  }
  .brand__name {
    color: var(--ink-light);
    font-family: var(--type-face);
    font-weight: 300;
    font-size: 36px; line-height: 1;
    white-space: nowrap;
  }
</style>
</head>
<body>
<main class="canvas">

  <section class="card card--front-white">
    <svg class="gear-artwork" viewBox="0 0 438 283" role="img" aria-label="Line illustration of interlocking clock gears in grey and red along the top and left edges">
      <defs>
        <linearGradient id="gears-on-white" x1="0" y1="0" x2="1" y2="1">
          <stop offset="0" stop-color="#e6e0e2"/>
          <stop offset="1" stop-color="#f3eef0"/>
        </linearGradient>
      </defs>
      <path d="M0 0 H438 V80 Q380 95 330 70 Q250 50 180 90 Q110 120 90 170 Q140 190 200 215 Q260 230 250 283 H0 Z" fill="url(#gears-on-white)"/>
    </svg>
    <div class="contact">
      <p class="contact__name">YOUR NAME HEAR</p>
      <p class="contact__phone">0000 999 999 999</p>
      <p class="contact__address">Address here Address here</p>
      <p class="contact__web">www.valtrion.com.sg</p>
      <p class="contact__email">Email here Email here</p>
    </div>
  </section>

  <section class="card card--front-red">
    <svg class="gear-artwork" viewBox="0 0 438 283" role="img" aria-label="Line illustration of interlocking clock gears in white and dark grey along the top and left edges">
      <defs>
        <linearGradient id="gears-on-red" x1="0" y1="0" x2="1" y2="1">
          <stop offset="0" stop-color="#a8394c"/>
          <stop offset="1" stop-color="#9d2538"/>
        </linearGradient>
      </defs>
      <path d="M0 0 H438 V80 Q380 95 330 70 Q250 50 180 90 Q110 120 90 170 Q140 190 200 215 Q260 230 250 283 H0 Z" fill="url(#gears-on-red)"/>
    </svg>
    <div class="contact">
      <p class="contact__name">YOUR NAME HEAR</p>
      <p class="contact__phone">0000 999 999 999</p>
      <p class="contact__address">Address here Address here</p>
      <p class="contact__web">www.valtrion.com.sg</p>
      <p class="contact__email">Email here Email here</p>
    </div>
  </section>

  <section class="card card--back">
    <div class="brand">
      <span class="brand__mark"></span>
      <span class="brand__name">VALTRION TOOLS</span>
    </div>
  </section>

</main>
</body>
</html>
```